Marlow Vista Magazine need Logo desing and front page for 1 edittion

This is a new magazine that will be circulating in Panama. the magazine will run non for profit,will be mostly informative and few advertizers to cover printing costs.
the magaine will oncce every 2 or 3 month. we need to present it to the editors who will be aproving or diss aproving the project.

we need a Logo desing for the name of the magazine "Marlow Vista" and the "front cover desing for the first edition" it will be good if the designer can incude the designed format for the iner magazine, for us just to add in the artucles and the spaces for advertizing.

the magazine content will be articles by govenment energy sectors, gloval warming articles, articles in renewvable enery, university profesor talking or promoting new ideas or university advances, orientations, special edition on book or international articles about the subject on saving enerty, different sectors, world innovations in renewbable energy, and the companies who will advertize will be comapnies selling QUIRT products, companies offfering product and services on renewvable energy, Led product and systems companies etc...

```html
<!DOCTYPE html>
<html lang="en">
<head>
<meta charset="utf-8">
<title>Marlow Vista — Feature Spread</title>
<link rel="stylesheet" href="https://fonts.googleapis.com/css2?family=Josefin+Sans:wght@400&family=Arimo:wght@400;700&display=swap">
<style>
  :root {
    --backdrop: #e8e8e8;
    --ink: #111111;
    --folio-grey: #7a7f86;
    --body-ink: #1a1a1a;
    --sky-light: #eef3f8;
    --sky-mid: #dfe7f0;
    --shirt-light: #f1f5fa;
    --shirt-shade: #c9d7e8;
    --grass: #2f8a22;
    --grass-light: #7dbf4a;
    --skin: #e2b3a0;
  }
  html, body {
    margin: 0;
    padding: 0;
    width: 1200px;
    height: 1000px;
    overflow: hidden;
    background: var(--backdrop);
  }
  .spread {
    position: absolute;
    left: 20px;
    top: 128px;
    width: 1148px;
    height: 742px;
    overflow: hidden;
    box-shadow: 2px 3px 4px rgba(0,0,0,0.35);
  }
  .spread__photo {
    position: absolute;
    inset: 0;
    background:
      radial-gradient(circle at 528px 380px, var(--grass) 0, var(--grass) 150px, var(--grass-light) 192px, rgba(125,191,74,0) 198px),
      radial-gradient(ellipse 250px 120px at 520px 560px, var(--skin) 0, var(--skin) 55%, rgba(226,179,160,0) 100%),
      radial-gradient(ellipse 110px 150px at 700px 520px, #d9a893 0, rgba(217,168,147,0) 100%),
      radial-gradient(ellipse 260px 420px at 760px 360px, var(--shirt-light) 0, rgba(241,245,250,0) 100%),
      radial-gradient(ellipse 280px 520px at 1010px 420px, var(--shirt-light) 0, var(--shirt-shade) 70%, rgba(201,215,232,0) 100%),
      linear-gradient(90deg, var(--sky-light) 0%, var(--sky-mid) 55%, #d6e1ee 100%);
  }
  .spread__gutter {
    position: absolute;
    left: 578px;
    top: 0;
    width: 4px;
    height: 742px;
  }
  .folio {
    position: absolute;
    top: 30px;
    font-family: "Arimo", Arial, sans-serif;
    font-size: 10px;
    color: var(--folio-grey);
    letter-spacing: 0.2px;
  }
  .folio__num { font-weight: 700; color: var(--ink); }
  .folio__rule { margin: 0 6px; }
  .folio--left { left: 31px; }
  .folio--right { right: 33px; }
  .feature__title {
    position: absolute;
    left: 33px;
    top: 64px;
    margin: 0;
    font-family: "Josefin Sans", "Futura", sans-serif;
    font-weight: 400;
    font-size: 86px;
    line-height: 102px;
    letter-spacing: 3px;
    color: var(--ink);
    text-transform: uppercase;
  }
  .feature__lede {
    position: absolute;
    left: 31px;
    top: 484px;
    width: 188px;
    margin: 0;
    font-family: "Arimo", Arial, sans-serif;
    font-size: 10.4px;
    line-height: 19.3px;
    color: var(--body-ink);
  }
</style>
</head>
<body>
  <article class="spread">
    <div class="spread__photo" role="img" aria-label="Photograph: an open hand holding a grass-covered globe, a man in a light blue shirt softly out of focus behind"></div>

    <svg class="spread__gutter" viewBox="0 0 4 742" aria-hidden="true">
      <line x1="2" y1="7" x2="2" y2="742" stroke="#222" stroke-width="2.6" stroke-dasharray="30 34"/>
    </svg>

    <div class="folio folio--left"><span class="folio__num">8</span><span class="folio__rule">|</span>MARLOW VISTA</div>
    <div class="folio folio--right">JANUARY 2014<span class="folio__rule">|</span><span class="folio__num">9</span></div>

    <h1 class="feature__title">USA<br>Green<br>With<br>Envy</h1>

    <p class="feature__lede">Exceperum lab ium qui rem fugitii sciliqui asi ant, quae. Et etum eariandit qui omnit, cus venturi aturepr aepuda quis esciduc iusant ut voles as. n exce-perum lab ium qui rem fugitii sciliqui asi ant, quae. Et etum eariandit qui omnit, cus venturi aturepr aepuda quis esciduc iusant ut voles as</p>
  </article>
</body>
</html>
```